Webstore needed

I am looking for someone to design a website/store for me. My website is called Silver Harbor Keepsakes. I currently have an under construction page up on my site and need to get my online store up asap. my domain is www.silverharborkeepsakes.com
Some comparison sites are

http://www.velmorecards.com
www.brightvaultgoods.com
www.kolbrandgear.com
www.lantrivo.com

Industry/Entity Type

Construction

Number of Pages Required

5+ page

Requirements
Must have
• I need to have a searchable database where customers will be able to verify items they purchase. A demo of the kind of database I will need can be found here: www.brightvaultgoodscheck.com
• input the number 41470 to see a sample item come up in the database.

```html
<!DOCTYPE html>
<html lang="en">
<head>
<meta charset="utf-8">
<title>Silver Harbor Keepsakes</title>
<link rel="stylesheet" href="https://fonts.googleapis.com/css2?family=Oswald:wght@400;500&family=Open+Sans:wght@400;600;800&family=Great+Vibes&display=swap">
<style>
:root{
  --bg:#000;
  --bar:#1c1c1c;
  --bar-dark:#141414;
  --line:#333;
  --gold:#e3a21f;
  --gold-soft:#d89a2a;
  --text:#fff;
  --muted:#bdbdbd;
  --grey:#8a8a8a;
  --red:#c8401d;
  --footer:#1a1a1a;
  --footer-bottom:#111;
}
*{margin:0;padding:0;box-sizing:border-box}
html,body{width:1023px;height:1200px;overflow:hidden;background:var(--bg)}
body{position:relative;font-family:"Open Sans",sans-serif;color:var(--text)}
.abs{position:absolute}
a{color:inherit;text-decoration:none}

/* top bar */
.topbar{left:0;top:0;width:1023px;height:54px;background:linear-gradient(#222,#181818);border-bottom:1px solid var(--line)}
.call{left:155px;top:12px;display:flex;align-items:center;gap:8px;font-weight:600;font-size:13px}
.call .label{color:var(--gold)}
.top-links{left:467px;top:22px;display:flex;gap:35px;font-size:8px;color:var(--muted);text-transform:uppercase}
.cart-box{left:739px;top:14px;width:130px;height:26px;border:1px solid #444;font-size:8px;color:var(--muted);display:flex;align-items:center;gap:8px;padding-left:12px}

/* nav */
.navband{left:0;top:54px;width:1023px;height:68px;background:linear-gradient(#1f1f1f,#151515);border-bottom:1px solid var(--line)}
.brand{left:154px;top:72px;font-family:"Oswald",sans-serif;font-weight:500;font-size:21px;color:var(--gold);letter-spacing:.3px}
.menu{left:386px;top:54px;display:flex;height:68px}
.menu a{width:121px;border-left:1px solid #3a3a3a;padding:16px 0 0 19px;font-family:"Oswald",sans-serif;line-height:1.2}
.menu a:last-child{border-right:1px solid #3a3a3a}
.menu small{display:block;font-size:12px;color:#fff}
.menu span{font-size:16px;color:var(--gold)}
.menu a.active{background:radial-gradient(ellipse at 50% 0,#4a3a1a 0,transparent 60%)}

/* hero */
.hero{left:154px;top:122px;width:716px;height:349px;background:radial-gradient(ellipse at 70% 35%,#b86a1a 0,#5a3a10 25%,transparent 55%),radial-gradient(ellipse at 30% 55%,#1f5a2f 0,#12341c 30%,transparent 55%),linear-gradient(#2a2410,#131310 60%,#0c0c0a)}
.hero-title{left:411px;top:297px;width:459px;height:61px;background:rgba(0,0,0,.75);font-family:"Open Sans",sans-serif;font-weight:800;font-size:36px;color:var(--gold);padding:8px 0 0 22px;white-space:nowrap;overflow:hidden}
.hero-sub{left:455px;top:363px;width:415px;height:60px;background:rgba(0,0,0,.7);font-family:"Oswald",sans-serif;font-size:12.5px;text-align:right;padding:14px 12px 0 0;line-height:1.45}
.hero-arrows{left:810px;top:433px;display:flex;gap:2px}
.hero-arrows span{width:20px;height:20px;background:var(--red);display:flex;align-items:center;justify-content:center}

/* promos */
.promo-store{left:154px;top:480px;width:353px;height:119px;background:#333}
.promo-photo{left:154px;top:480px;width:118px;height:119px;background:linear-gradient(90deg,#6c6c6c,#3f3f3f)}
.store-head{left:281px;top:497px;display:flex;align-items:baseline;gap:8px}
.store-head .script{font-family:"Great Vibes",cursive;font-size:30px;color:#fff}
.store-head .shop{font-family:"Oswald",sans-serif;font-size:17px;color:var(--gold)}
.store-line{left:281px;top:536px;font-family:"Oswald",sans-serif;font-size:17px;letter-spacing:.5px}
.store-more{left:283px;top:566px;font-size:9px;color:var(--gold);display:flex;align-items:center;gap:5px}
.promo-offer{left:516px;top:480px;width:354px;height:119px;background:linear-gradient(90deg,#8b6c2c,#b7903f 45%,#6a4a20 75%,#3a2410)}
.offer-text{left:540px;top:508px;width:200px;text-align:center;color:#1a1a1a;font-family:"Oswald",sans-serif;line-height:1.2}
.offer-text .a{font-size:14px}
.offer-text .b{font-family:"Open Sans",sans-serif;font-weight:800;font-size:24px;color:#fff}
.offer-text .c{font-size:13px}

/* products */
.section-title{left:154px;top:624px;font-family:"Oswald",sans-serif;font-size:17px;color:var(--gold)}
.prod-arrows{left:824px;top:624px;display:flex;gap:2px}
.prod-arrows span{width:21px;height:21px;background:#222;display:flex;align-items:center;justify-content:center}
.products{left:154px;top:666px;width:716px;display:flex;justify-content:space-between}
.card{width:172px;text-align:center}
.card .thumb{height:155px}
.card h3{margin-top:16px;font-family:"Oswald",sans-serif;font-weight:400;font-size:12px;color:var(--gold)}
.card p{margin-top:4px;font-size:8px;color:var(--grey)}
.card .price{margin-top:4px;font-size:14px;color:var(--gold)}
.card .btn{display:inline-block;margin-top:8px;width:104px;height:26px;line-height:24px;border:1px solid var(--gold);font-size:8.5px;color:var(--gold)}

/* footer */
.footer{left:0;top:975px;width:1023px;height:183px;background:var(--footer)}
.fcol{top:1002px}
.fcol h4{font-family:"Oswald",sans-serif;font-weight:400;font-size:12px;color:var(--gold);margin-bottom:7px}
.fcol li{list-style:none;font-size:8px;color:#ccc;line-height:17.6px}
.footer-bottom{left:0;top:1158px;width:1023px;height:42px;background:var(--footer-bottom);display:flex;align-items:center;padding-left:155px;font-size:7.5px;color:#bbb;gap:14px}
.social{left:741px;top:1174px;display:flex;gap:18px}
.social span{width:11px;height:11px;border-radius:50%;background:#777}
</style>
</head>
<body>

<header>
  <div class="abs topbar"></div>
  <div class="abs call">
    <svg width="18" height="30" viewBox="0 0 18 30"><rect x="1.5" y="1.5" width="15" height="27" rx="2" fill="none" stroke="#e3a21f" stroke-width="2.5"/><line x1="1.5" y1="23" x2="16.5" y2="23" stroke="#e3a21f" stroke-width="2"/></svg>
    <span><span class="label">CALL US :</span> ( 1300) 482 915</span>
  </div>
  <nav class="abs top-links"><a href="#">My Account</a><a href="#">My Cart</a><a href="#">Login</a><a href="#">Register</a></nav>
  <div class="abs cart-box">
    <svg width="10" height="9" viewBox="0 0 10 9"><path d="M0 1h2l1.5 5h5L10 2.5H3" fill="none" stroke="#ccc" stroke-width="1"/><circle cx="4" cy="8" r=".9" fill="#ccc"/><circle cx="8" cy="8" r=".9" fill="#ccc"/></svg>
    YOUR CART IS : 0 ITEMS
  </div>

  <div class="abs navband"></div>
  <div class="abs brand">SILVER HARBOR KEEPSAKES</div>
  <nav class="abs menu">
    <a href="#" class="active"><small>VIEW OUR</small><span>ATHLETES</span></a>
    <a href="#"><small>FAVORITE</small><span>SPORTS</span></a>
    <a href="#"><small>EVENT</small><span>MEMORABILIA</span></a>
    <a href="#"><small>RECENT</small><span>AUCTIONS</span></a>
  </nav>
</header>

<main>
  <section>
    <div class="abs hero" role="img" aria-label="Football player in a green jersey running with the ball in a floodlit stadium"></div>
    <h1 class="abs hero-title">WE SELL SPORTS ACC</h1>
    <p class="abs hero-sub">LOREM IPSUM IS SIMPLY DUMMY TEXT OF THE PRINTING AND TYPESETTING.<br>LOREM IPSUM HAS BEEN THE INDUSTRY'S STANDARD</p>
    <div class="abs hero-arrows">
      <span><svg width="8" height="10"><path d="M6 1L2 5l4 4" fill="none" stroke="#fff" stroke-width="1.3"/></svg></span>
      <span><svg width="8" height="10"><path d="M2 1l4 4-4 4" fill="none" stroke="#fff" stroke-width="1.3"/></svg></span>
    </div>
  </section>

  <section>
    <div class="abs promo-store"></div>
    <div class="abs promo-photo" role="img" aria-label="Hockey player in a helmet with a clear visor"></div>
    <div class="abs store-head"><span class="script">Store</span><span class="shop">Shop Online</span></div>
    <div class="abs store-line">LOREM IPSUM IS A DUMMY</div>
    <a href="#" class="abs store-more">CLICK HERE FOR MORE INFO
      <svg width="11" height="11"><circle cx="5.5" cy="5.5" r="4.5" fill="none" stroke="#e3a21f" stroke-width="1"/><path d="M4.5 3.5l2.2 2-2.2 2" fill="none" stroke="#e3a21f" stroke-width="1"/></svg>
    </a>

    <div class="abs promo-offer" role="img" aria-label="Football and helmet on a warm gold background"></div>
    <div class="abs offer-text"><div class="a">LOREM IPSUM IS</div><div class="b">10% OFFER</div><div class="c">FOR SPECIAL PRODUCTS</div></div>
  </section>

  <section>
    <h2 class="abs section-title">OUR PRODUCTS</h2>
    <div class="abs prod-arrows">
      <span><svg width="8" height="10"><path d="M6 1L2 5l4 4" fill="none" stroke="#666" stroke-width="1"/></svg></span>
      <span><svg width="8" height="10"><path d="M2 1l4 4-4 4" fill="none" stroke="#666" stroke-width="1"/></svg></span>
    </div>
    <div class="abs products">
      <article class="card"><div class="thumb" role="img" aria-label="Pair of colourful running shoes" style="background:radial-gradient(circle at 35% 40%,#6a5a20,#1a1408 70%)"></div><h3>LOREM IPSUM IS SIMPLY</h3><p>Lorem Ipsum is simply dummy text</p><div class="price">$25.00</div><a href="#" class="btn">VIEW DETAILS</a></article>
      <article class="card"><div class="thumb" role="img" aria-label="Head protection cap seen from behind" style="background:linear-gradient(#2a2a2a,#555 50%,#1e1e1e)"></div><h3>LOREM IPSUM IS SIMPLY</h3><p>Lorem Ipsum is simply dummy text</p><div class="price">$25.00</div><a href="#" class="btn">VIEW DETAILS</a></article>
      <article class="card"><div class="thumb" role="img" aria-label="Black sports wristwatch" style="background:radial-gradient(circle at 40% 50%,#3a3a3a,#0e0e0e 65%,#d8d8d8 100%)"></div><h3>LOREM IPSUM IS SIMPLY</h3><p>Lorem Ipsum is simply dummy text</p><div class="price">$25.00</div><a href="#" class="btn">VIEW DETAILS</a></article>
      <article class="card"><div class="thumb" role="img" aria-label="Grey spotted football helmet" style="background:radial-gradient(circle at 50% 45%,#8a8a8a,#3a3a3a 60%,#1a1a1a)"></div><h3>LOREM IPSUM IS SIMPLY</h3><p>Lorem Ipsum is simply dummy text</p><div class="price">$25.00</div><a href="#" class="btn">VIEW DETAILS</a></article>
    </div>
  </section>
</main>

<footer>
  <div class="abs footer"></div>
  <div class="abs fcol" style="left:170px"><h4>WELCOME</h4><ul><li>HOME</li><li>ABOUT</li><li>CUSTOMER SERVICE</li><li>SEARCH TERMS</li></ul></div>
  <div class="abs fcol" style="left:331px"><h4>CUSTOMER SUPPORT</h4><ul><li>HELP CENTER</li><li>CONTACT US</li><li>SIZE CHARTS</li><li>RETURN POLICY</li><li>SHIPPING INFO</li><li>SITE MAP</li></ul></div>
  <div class="abs fcol" style="left:528px"><h4>OUR PRODUCTS</h4><ul><li>BULLETPROOF VESTS</li><li>PROTECTIVE ARMOR PLATES</li><li>BALLISTIC HELMETS</li><li>MILITARY UNIFORMS</li><li>MAGAZINES</li><li>MILITARY BACKPACKS.</li></ul></div>
  <div class="abs fcol" style="left:733px"><h4>MY ACCOUNT</h4><ul><li>SIGN IN</li><li>VIEW CART</li><li>MY WISHLIST</li><li>TRACK MY ORDER</li><li>HELP</li></ul></div>
  <div class="abs footer-bottom">
    <span>© COPYRIGHT. SILVER HARBOR KEEPSAKES 2014. ALL RIGHTS RESERVED.</span><span>|</span><span>PRIVACY POLICY</span><span>|</span><span>SITE MAP</span><span>|</span><span>TERMS &amp; CONDITIONS</span>
  </div>
  <div class="abs social" aria-label="Social links"><span></span><span></span><span></span><span></span><span></span></div>
</footer>

</body>
</html>
```